Inspiration Poster

Inspirational Poster that has a Kamran Dulo like abstract look (http://www.vexalo.com/images/search?q=kamran+dulo&FORM=HDRSC2) with the text:

"we walk not in order to arrive at the promise land but because walking itself is a revolution"
-Peter Ambrick

```html
<!DOCTYPE html>
<html lang="en">
<head>
<meta charset="utf-8">
<title>Inspiration Poster</title>
<link rel="stylesheet" href="https://fonts.googleapis.com/css2?family=Oswald:wght@600;700&display=swap">
<style>
  :root {
    --quote-red: #c9202e;
    --type-white: #ffffff;
    --sky-blue: #5e93d6;
    --ice-blue: #a9d4ea;
    --deep-navy: #1d2c5c;
    --ink-dark: #1a1c2a;
    --bokeh-green: #7be07a;
    --bokeh-pink: #d8306e;
    --violet: #7b3fd0;
  }
  html, body {
    margin: 0;
    padding: 0;
    width: 907px;
    height: 1200px;
    overflow: hidden;
    background: #ffffff;
  }
  .poster {
    position: relative;
    width: 907px;
    height: 1200px;
    overflow: hidden;
    font-family: "Oswald", "Arial Narrow", sans-serif;
  }
  .poster-artwork {
    position: absolute;
    inset: 0;
    background:
      radial-gradient(circle at 90% 6%, rgba(123, 63, 208, 0.75) 0, rgba(123, 63, 208, 0) 18%),
      radial-gradient(circle at 38% 68%, rgba(123, 224, 122, 0.85) 0, rgba(123, 224, 122, 0) 14%),
      radial-gradient(circle at 20% 90%, rgba(123, 224, 122, 0.8) 0, rgba(123, 224, 122, 0) 16%),
      radial-gradient(circle at 55% 74%, rgba(216, 48, 110, 0.8) 0, rgba(216, 48, 110, 0) 16%),
      radial-gradient(circle at 75% 86%, rgba(123, 224, 122, 0.55) 0, rgba(123, 224, 122, 0) 12%),
      radial-gradient(circle at 80% 55%, rgba(40, 40, 60, 0.85) 0, rgba(40, 40, 60, 0) 30%),
      linear-gradient(180deg,
        var(--sky-blue) 0%,
        var(--ice-blue) 20%,
        #7ab0d8 34%,
        #4a6fae 44%,
        var(--deep-navy) 50%,
        #3f5a6c 64%,
        #3a4850 82%,
        var(--ink-dark) 100%);
  }
  .quote {
    position: absolute;
    left: 68px;
    top: 86px;
    margin: 0;
    width: 820px;
    color: var(--quote-red);
    font-weight: 700;
    font-size: 61px;
    line-height: 74px;
    text-transform: uppercase;
    letter-spacing: 0.2px;
    text-shadow: 2px 2px 0 var(--type-white), -1px -1px 0 var(--type-white), 1px -1px 0 var(--type-white), -1px 1px 0 var(--type-white);
  }
  .quote-mark {
    font-size: 56px;
    vertical-align: top;
    line-height: 50px;
  }
  .quote-mark.open {
    position: absolute;
    left: -38px;
    top: 2px;
  }
  .quote-mark.close {
    margin-left: 8px;
  }
  .attribution {
    position: absolute;
    right: 72px;
    top: 492px;
    margin: 0;
    color: var(--type-white);
    font-weight: 600;
    font-size: 33px;
    line-height: 40px;
    text-transform: uppercase;
  }
</style>
</head>
<body>
  <main class="poster">
    <div class="poster-artwork" role="img" aria-label="Abstract photo of hands overlaid with pixel squares and glowing green and pink bokeh lights, blue at the top fading to dark below"></div>
    <blockquote class="quote">
      <span class="quote-mark open">“</span>We walk not in order<br>
      to arrive at the promise<br>
      land but because walking<br>
      itself is a revolution<span class="quote-mark close">”</span>
    </blockquote>
    <p class="attribution">- Peter Ambrick</p>
  </main>
</body>
</html>
```